Brindlecove Business Card

Looking for a new business Card layout for our company, brindlecove.

Logo Text

Standard Business Card , Name, email, phone, website. www.brindlecove-example.com

```html
<!DOCTYPE html>
<html lang="en">
<head>
<meta charset="utf-8">
<title>Brindlecove Business Card</title>
<link rel="stylesheet" href="https://fonts.googleapis.com/css2?family=Open+Sans:wght@700&display=swap">
<style>
  :root {
    --slate: #5d6880;
    --sky: #55b5dc;
    --paper: #ffffff;
  }
  html, body {
    margin: 0;
    padding: 0;
    overflow: hidden;
    background: var(--paper);
  }
  .card {
    position: relative;
    width: 1200px;
    height: 686px;
    overflow: hidden;
    background: var(--paper);
    font-family: "Open Sans", Arial, sans-serif;
    font-weight: 700;
  }
  .decoration {
    position: absolute;
    left: 705px;
    top: 176px;
    width: 495px;
    height: 510px;
    border-top-left-radius: 260px 240px;
    background:
      radial-gradient(circle at 18% 38%, var(--sky) 0 28%, transparent 46%),
      radial-gradient(circle at 78% 40%, var(--slate) 0 34%, transparent 60%),
      linear-gradient(135deg, var(--sky) 0%, #6f8fb2 50%, var(--slate) 100%);
    opacity: 0.95;
  }
  .contact-panel {
    position: absolute;
    left: 46px;
    top: 57px;
    width: 788px;
    height: 423px;
    background: var(--slate);
    color: var(--paper);
  }
  .contact-panel .name {
    position: absolute;
    left: 60px;
    top: 103px;
    margin: 0;
    font-size: 112px;
    line-height: 1;
    letter-spacing: 5px;
    font-weight: 700;
  }
  .contact-list {
    position: absolute;
    left: 60px;
    top: 249px;
    margin: 0;
    padding: 0;
    list-style: none;
    font-size: 38px;
    letter-spacing: 1.5px;
    line-height: 58px;
  }
  .brand-name {
    position: absolute;
    left: 46px;
    top: 574px;
    margin: 0;
    font-size: 44px;
    line-height: 1;
    letter-spacing: 0;
    color: var(--sky);
    text-transform: uppercase;
  }
</style>
</head>
<body>
  <main class="card">
    <div class="decoration" role="img" aria-label="Abstract fluid blob shapes in sky blue and slate"></div>
    <section class="contact-panel">
      <h1 class="name">John Doe</h1>
      <ul class="contact-list">
        <li class="email">johndoe@brindlecove.com</li>
        <li class="phone">555-010-4821</li>
        <li class="website">www.brindlecove-example.com</li>
      </ul>
    </section>
    <p class="brand-name">Brindlecove</p>
  </main>
</body>
</html>
```